halbrook paving works

Needs to have phone number 0418352790 and email carlwhitby@mailnest.com.au.
ABN 27813046652
name carl whitby

For all your concreting solutions
Excavation
Exposed & colour concrete
House & shed slabs
Driveways
Landing & steps

Contact Information for Business Card

ph 0418352790
email carlwhitby@mailnest.com.au.
ABN 27813046652
name carl whitby

```html
<!DOCTYPE html>
<html lang="en">
<head>
<meta charset="utf-8">
<title>Halbrook Paving Works – Business Card</title>
<link href="https://fonts.googleapis.com/css2?family=Montserrat:wght@400;500;600;700&display=swap" rel="stylesheet">
<style>
  :root {
    --bg: #e4e3e0;
    --card-white: #ffffff;
    --charcoal: #3d4144;
    --charcoal-dark: #34383b;
    --orange: #e8772a;
    --ink: #2b2b2b;
    --grey-text: #6b6e70;
    --light: #f2f2f2;
  }
  * { box-sizing: border-box; margin: 0; padding: 0; }
  html, body { width: 1200px; height: 875px; overflow: hidden; }
  body {
    background: var(--bg);
    font-family: "Montserrat", Arial, sans-serif;
    position: relative;
  }
  .card {
    position: absolute;
    left: 300px;
    width: 600px;
    height: 340px;
    overflow: hidden;
    box-shadow: 0 6px 18px rgba(0,0,0,0.12);
  }
  /* ---------- front ---------- */
  .card-front { top: 60px; background: var(--card-white); }
  .brand {
    position: absolute;
    display: flex;
    align-items: center;
  }
  .brand-mark {
    background: var(--orange);
    flex: none;
  }
  .brand-text { border-left: 2px solid var(--orange); }
  .brand-name {
    color: var(--orange);
    font-weight: 600;
    letter-spacing: 0.02em;
    white-space: nowrap;
  }
  .brand-phone {
    color: var(--orange);
    font-weight: 500;
    letter-spacing: 0.14em;
  }
  .card-front .brand { left: 40px; top: 58px; }
  .card-front .brand-mark { width: 46px; height: 46px; margin-right: 12px; }
  .card-front .brand-text { padding-left: 10px; }
  .card-front .brand-name { font-size: 14px; }
  .card-front .brand-phone { font-size: 10px; margin-top: 3px; }

  .holder {
    position: absolute;
    right: 58px;
    top: 108px;
    font-size: 21px;
    font-weight: 600;
    color: var(--ink);
  }
  .contact-list {
    position: absolute;
    right: 40px;
    top: 158px;
    list-style: none;
    text-align: right;
  }
  .contact-item {
    display: flex;
    justify-content: flex-end;
    align-items: center;
    gap: 10px;
    font-size: 14px;
    color: var(--ink);
    letter-spacing: 0.02em;
    line-height: 1;
    margin-bottom: 9px;
  }
  .contact-icon { width: 14px; height: 14px; flex: none; }
  .front-band {
    position: absolute;
    left: 0; right: 0; bottom: 0;
    height: 74px;
    background: var(--charcoal);
    display: flex;
    align-items: flex-end;
    padding: 0 0 18px 38px;
  }
  .abn {
    color: var(--light);
    font-size: 12px;
    letter-spacing: 0.08em;
  }
  /* ---------- back ---------- */
  .card-back {
    top: 470px;
    background: linear-gradient(160deg, var(--charcoal) 0%, var(--charcoal-dark) 100%);
  }
  .card-back .brand { left: 110px; top: 90px; }
  .card-back .brand-mark { width: 80px; height: 80px; margin-right: 20px; }
  .card-back .brand-text { padding: 6px 0 6px 14px; }
  .card-back .brand-name { font-size: 24px; }
  .card-back .brand-phone { font-size: 16px; margin-top: 6px; }
  .services {
    position: absolute;
    left: 40px; right: 40px;
    top: 236px;
    text-align: center;
    color: var(--light);
    font-size: 11.5px;
    font-weight: 500;
    line-height: 1.5;
  }
</style>
</head>
<body>

  <section class="card card-front">
    <div class="brand">
      <div class="brand-mark"></div>
      <div class="brand-text">
        <div class="brand-name">HALBROOK PAVING WORKS</div>
        <div class="brand-phone">0418352790</div>
      </div>
    </div>

    <div class="holder">Carl Whitby</div>

    <ul class="contact-list">
      <li class="contact-item">0418 352 790
        <svg class="contact-icon" viewBox="0 0 14 14" aria-hidden="true">
          <circle cx="7" cy="7" r="7" fill="var(--orange)"/>
          <path d="M4.6 3.8 L5.8 3.6 L6.4 5.2 L5.6 5.8 Q6.3 7.5 8.2 8.4 L8.8 7.6 L10.4 8.2 L10.2 9.4 Q9.6 10.3 8.4 10 Q4.8 8.8 4 5.6 Q3.9 4.4 4.6 3.8Z" fill="#fff"/>
        </svg>
      </li>
      <li class="contact-item">carlwhitby@mailnest.com.au
        <svg class="contact-icon" viewBox="0 0 14 14" aria-hidden="true">
          <circle cx="7" cy="7" r="7" fill="var(--orange)"/>
          <rect x="3.5" y="4.5" width="7" height="5" rx="0.6" fill="#fff"/>
          <path d="M3.7 4.8 L7 7.3 L10.3 4.8" fill="none" stroke="var(--orange)" stroke-width="0.9"/>
        </svg>
      </li>
      <li class="contact-item">halbrookpavingworks.com.au
        <svg class="contact-icon" viewBox="0 0 14 14" aria-hidden="true">
          <circle cx="7" cy="7" r="7" fill="var(--orange)"/>
          <circle cx="7" cy="7" r="3.6" fill="none" stroke="#fff" stroke-width="1"/>
          <path d="M3.4 7 H10.6 M7 3.4 Q5.2 7 7 10.6 M7 3.4 Q8.8 7 7 10.6" fill="none" stroke="#fff" stroke-width="0.8"/>
        </svg>
      </li>
    </ul>

    <div class="front-band">
      <span class="abn">ABN 27813046652</span>
    </div>
  </section>

  <section class="card card-back">
    <div class="brand">
      <div class="brand-mark"></div>
      <div class="brand-text">
        <div class="brand-name">HALBROOK PAVING WORKS</div>
        <div class="brand-phone">0418352790</div>
      </div>
    </div>

    <p class="services">
      For all your Concreting Solutions, Excavation, Exposed &amp; Colour Concrete,<br>
      House &amp; Shed Slabs, Driveways, Landing &amp; Steps
    </p>
  </section>

</body>
</html>
```